7bandits!thefilm

Design "hot" movie poster for a new comedy feature film

www.7banditsthefilm.example
(pictures off the media page)
www.whynotbecomeabandit.example
www.pinbloq.example/blog/7banditsthefilm

Key tips:
1. hype – comedy of our time, parody of reality tv - Xtreme Shock & awe(some) fun
2. comedy first, entertainment focused at all times. Bright not dark. Funny not serious. Push the boundaries. Think outside the square. Make people sit up and laugh, then wonder and then laugh again.

Our Story:
A shock & awe(some) comedy about the absurdity of reality TV and our insatiable desire for the Xtreme.
In this irresistible, high-octane comedy, a Los Angeles producer steals from popular Reality TV formats, hiring three judges (an ex-MI6 agent, explosives expert and FARC commander) to seek out the ultimate amateur master terrorist. The 10 wannabe finalists try their luck in out-of-control challenges and eliminations in his version of Why Not Become A Bandit!, The Loaded Understudy, Boomkitchen and Fab Snoop for the Outlaw Troop. The producer wants action and explosions, even if this means contestants might get killed! But while eyes are diverted, a failed contestant hacks the show, giving everyone more than they bargained for. 7bandits! is a parody of the world we ‘occupy’ and speaks directly into our media-saturated 21st century.

Tagline
A Shock and Awe(some) comedy

Seeking design CONCEPT and we will consider who should do the poster for international theatrical and digital release.

I have attached an old flyer - but this may NOT help in ideas. We are short of iconic poster images.

Have extended budget. Thanks to designers

Reason: We have added a second prize as well - and added two days. Hope this works for you designers. Thanks Wyn

The submissions have been so great - a big THANKS you to all designers. It's 1 Feb already in Australia - and I'll work out shortly how we go from here. 

Target Market(s)

Gen y, students
socio-political aware group - harvest of lies follows, occupy
ethnic groups

Industry/Entity Type

Entertainment

Requirements
Must have
• not too busy...
Nice to have
• maybe this quote...

“Seriously stupid,
Absurdly clever,
Best comedy this year”
DAILY GLOBE POST

Needs to have space for typical credit block of names - that we can provide... It will also have to space / consideration for 4 logos - MA15+ logo, comedy festival logo, co. logo etc

Should not have
• I have attached an old flyer - but this may not help in ideas

```html
<!DOCTYPE html>
<html lang="en">
<head>
<meta charset="utf-8">
<title>7bandits! flyer</title>
<link rel="stylesheet" href="https://fonts.googleapis.com/css2?family=Black+Ops+One&family=Rye&family=Arimo:wght@400;700&family=Alfa+Slab+One&family=Cormorant+Garamond:wght@500&display=swap">
<style>
:root{
  --page:#ffffff;
  --rust-dark:#3a1c0c;
  --rust:#7a3d17;
  --rust-light:#a3602a;
  --band:#1c1410;
  --ink-light:#ffffff;
  --accent-yellow:#f5e21b;
  --accent-red:#c41d1d;
  --body-text:#f1e6d8;
}
*{margin:0;padding:0;box-sizing:border-box}
html,body{width:1200px;height:1161px;overflow:hidden;background:var(--page)}
.canvas{position:relative;width:1200px;height:1161px}
.panel{position:absolute;left:19px;width:1158px;height:551px;overflow:hidden;
  background:radial-gradient(ellipse at 40% 50%,var(--rust-light) 0%,var(--rust) 45%,var(--rust-dark) 100%)}
.panel--front{top:19px}
.panel--back{top:587px}
.title-band{position:absolute;background:var(--band);padding:10px 26px;
  box-shadow:0 0 24px rgba(0,0,0,.6)}
.title{font-family:"Black Ops One",system-ui,sans-serif;color:var(--ink-light);
  font-size:96px;line-height:1;letter-spacing:2px;white-space:nowrap}
.title .slash{color:var(--accent-red)}
.front-title{left:58px;top:30px}
.back-title{left:56px;top:32px}
.site-url{position:absolute;right:26px;top:18px;font-family:"Arimo",Arial,sans-serif;
  font-weight:700;font-size:13px;color:var(--ink-light)}
.hero-photo{position:absolute;left:620px;top:0;width:538px;height:551px;
  background:linear-gradient(110deg,rgba(58,28,12,0) 0%,#5a3220 30%,#3b2218 55%,#6a6f78 75%,#2a1a12 100%)}
.press-quote{position:absolute;left:72px;top:345px;font-family:"Rye",Georgia,serif;
  color:var(--ink-light);font-size:33px;line-height:41px;text-transform:uppercase}
.press-source{position:absolute;left:72px;top:484px;font-family:"Rye",Georgia,serif;
  color:var(--ink-light);font-size:17px}
.scene-photo{position:absolute;left:69px;top:178px;width:505px;height:325px;
  border:3px solid #1a120d;
  background:radial-gradient(ellipse at 62% 30%,#e9e6c8 0%,#8c8a6c 18%,#4a3f2c 45%,#1e1611 100%)}
.synopsis{position:absolute;left:662px;top:30px;width:470px;color:var(--body-text)}
.synopsis-heading{font-family:"Rye",Georgia,serif;font-style:italic;color:var(--ink-light);
  font-size:23px;line-height:30px;text-transform:uppercase;font-weight:400}
.synopsis-body{margin-top:16px;font-family:"Arimo",Arial,sans-serif;font-size:15.2px;line-height:22.6px}
.synopsis-body .show-name{color:var(--accent-yellow);font-weight:700}
.review-quote{margin-top:18px;font-family:"Arimo",Arial,sans-serif;font-style:italic;font-size:15px;line-height:22px}
.reviewer{margin-top:4px;display:flex;align-items:center;gap:10px;
  font-family:"Alfa Slab One",Georgia,serif;color:var(--accent-yellow);font-size:19px}
.stars{letter-spacing:4px;font-size:18px}
.logo-slot{position:absolute;left:662px;top:438px;width:467px;height:80px;background:#ffffff;
  display:flex;align-items:center;justify-content:center;
  font-family:"Cormorant Garamond",Georgia,serif;font-weight:500;font-size:20px;color:#111}
</style>
</head>
<body>
<div class="canvas">
  <section class="panel panel--front">
    <div class="hero-photo" role="img" aria-label="Photo of a grinning contestant shouldering a rocket launcher"></div>
    <div class="title-band front-title"><h1 class="title">7BANDITS!</h1></div>
    <p class="site-url">www.7banditsthefilm.example</p>
    <p class="press-quote">“Seriously stupid,<br>absurdly clever,<br>best comedy this year”</p>
    <p class="press-source">DAILY GLOBE POST</p>
  </section>

  <section class="panel panel--back">
    <div class="title-band back-title"><h2 class="title">7BANDITS!</h2></div>
    <div class="scene-photo" role="img" aria-label="Film still of contestants in orange jumpsuits in a dim cell under a hanging lamp"></div>
    <div class="synopsis">
      <h3 class="synopsis-heading">High-octane comedy questioning the world we live in!</h3>
      <p class="synopsis-body">Shady Los Angeles producer, Rex D, will do anything for a ratings bonanza, rolling out the most extreme reality show ever: <span class="show-name">Who Wants To Be A Bandit!</span> Stealing from popular formats (Loaded Understudy, Fab Snoop for the Outlaw Troop, Boomkitchen), three Judges set out to find the amateur master-bandit through a series of out-of-control challenges and eliminations, using interrogation and even torture. But they get way more than they bargained for.</p>
      <p class="review-quote">“like Corvell's film (Dr Doomsday), it's damn funny, the sort of qualities that money can't buy”</p>
      <p class="reviewer"><span>Harold Wetherby FILMOSCOPE.</span><span class="stars">★★★★</span></p>
    </div>
    <div class="logo-slot">LOGOS</div>
  </section>
</div>
</body>
</html>
```